Large corporation needs landing page for its employees with emotional and psychological problems

Vision:
Hello, we are a startup and would like to build a landing page and website in the mental health sector for a large corporation. In this site employees with emotional and psychological problems should quickly receive professional psychological support. This support takes the form of internal referrals from employees who are looking for help to qualified therapists, so that help can be provided quickly.
Furthermore, the employees get access to a tool where they can find out about topics in the mind health area and can also get help via webinars and podcasts. The employee should thus be able to take the hurdle to seek help and support in good time.
Therapists for whom the focus is on the urgency of providing quick help and support will work here in cooperation with the respective corporations.
Keywords:
• Help/Support
• overcome inhibitions
• Competent help
• Uncomplicated help
• Permanent access
• protected space
• Recognizing and naming emotional problems and actively tackling them
• get help
• mindfulness
• everyday helper
• Informative
• Anonymous
• compassion
• tolerance
• respect
• Appreciation
• empathy
• mindfulness
• protected space
• To be needed
• Like a lighthouse signal
What we need:
Landingpage
We need a landing page aimed at getting employees to contact psychological help. The call to action is to get in contact via a contact form.
Landing page content
There are several text modules:
• A heading/greeting
• A body of text at the beginning that explains the purpose of the page
• A bulleted text area describing the pain points and the solutions to them
Video:
The heart of the content will be a video explaining the need and inviting them to get in touch.
contact form:
It should be kept simple: first name, last name and email address
Legally required content:
General terms and conditions, data protection and imprint. These are only given as links in the footer.
In parallel, the Corporate Design should be adapted/extended:
Logo:
The font in the logo should be revised. The wings in the background remain.
Please adapt the logo for different uses:
• on a black background
• with transparent background
• favorite icon (browser)
• In square format for social media
Colors:
• develop a color chart based on the colors of the logo.
• please determine 2-3 main colors and the matching variations. I.e. transparent variations or light colors.
Typography:
Determine a decorative font and/or typography for headings and a text font. There should be no more than 3 fonts.
Updates
Need extra days to review
Industry/Entity Type
to recruit therapists as employees
Should not have
- please not to playful design or typography - and max. 3 colors

```html
<!DOCTYPE html>
<html lang="en">
<head>
<meta charset="utf-8">
<title>Calm Harbor – Emotional and Psychological Support</title>
<link href="https://fonts.googleapis.com/css2?family=Poppins:wght@500;600;700;800&family=Mulish:wght@400;500;600;700&display=swap" rel="stylesheet">
<style>
:root{
  --ink:#1f3b3c;
  --brand:#1e4b55;
  --btn:#223f3b;
  --mist:#eef7fa;
  --sky:#add5e1;
  --text:#333b3d;
  --muted:#5b6668;
  --red:#e2453b;
  --white:#ffffff;
  --line:#34505a;
}
*{box-sizing:border-box;margin:0;padding:0}
html,body{width:1200px;height:3449px;overflow:hidden;background:var(--white)}
body{font-family:"Mulish",sans-serif;color:var(--text);position:relative}
section,header,footer{position:absolute;left:0;width:1200px}
.abs{position:absolute}
h2{font-family:"Poppins",sans-serif;color:var(--ink);font-weight:600;letter-spacing:.3px}
.rule{display:block;height:3px;background:var(--brand)}
.btn{position:absolute;background:var(--btn);color:var(--white);font-family:"Poppins",sans-serif;font-weight:600;display:flex;align-items:center;justify-content:center;text-transform:uppercase}

/* header */
.site-header{top:0;height:74px;display:flex;align-items:center;justify-content:center}
.brand-name{font-family:"Poppins",sans-serif;font-weight:600;color:var(--brand);font-size:28px;display:flex;align-items:center;gap:8px}
.brand-dot{width:12px;height:12px;border-radius:50%;background:#8fc3d2}

/* hero */
.hero{top:74px;height:537px;background:linear-gradient(100deg,#5b4a3e 0%,#8b7565 35%,#c9a9a8 65%,#e8c9cd 100%)}
.hero-play{left:574px;top:278px;width:52px;height:52px}
.hero-title{left:320px;top:368px;width:560px;border-top:2px solid rgba(255,255,255,.85);border-bottom:2px solid rgba(255,255,255,.85);padding:6px 0 8px;text-align:center;color:var(--white);font-family:"Poppins",sans-serif;font-weight:800;font-size:31px;letter-spacing:-.3px}

/* welcome */
.welcome{top:611px;height:475px;background:var(--mist)}
.welcome-kicker{left:134px;top:64px;font-size:19px;font-weight:600}
.welcome-title{left:134px;top:90px;font-size:25px;font-weight:700}
.welcome .rule{left:134px;top:138px;width:82px}
.welcome-copy{left:135px;top:172px;width:394px;font-size:12.4px;line-height:19.2px;text-align:justify;color:#3a3f40}
.welcome .btn{left:137px;top:380px;width:104px;height:34px;font-size:11.5px}
.welcome-photo{left:590px;top:62px;width:479px;height:355px;background:linear-gradient(135deg,#6b5646 0%,#a58e78 40%,#3f4a3e 100%)}

/* therapists */
.therapists{top:1086px;height:538px}
.section-title{width:1200px;left:0;text-align:center;font-size:19.5px;font-weight:600}
.section-rule{left:587px;width:28px;height:3px;background:var(--brand)}
.therapists .section-title{top:44px}
.therapists .section-rule{top:88px}
.carousel-arrow{top:286px;width:22px;height:30px}
.therapist-card{top:124px;width:224px;height:362px;border:1px solid var(--line);background:var(--white)}
.therapist-photo{width:100%;height:158px}
.therapist-name{position:absolute;left:23px;top:180px;font-family:"Poppins",sans-serif;font-weight:600;font-size:14px;color:var(--ink)}
.therapist-role{position:absolute;left:23px;top:200px;font-size:11px;color:var(--muted)}
.therapist-bio{position:absolute;left:23px;top:230px;width:170px;font-size:10.5px;line-height:14px;color:#444}
.therapist-card .btn{left:25px;top:307px;width:70px;height:26px;font-size:9px}

/* podcasts */
.podcasts{top:1624px;height:737px;background:var(--sky)}
.podcasts .section-title{top:40px}
.podcasts .section-rule{top:84px}
.episode{width:457px;height:113px;background:var(--white);display:flex}
.episode-photo{width:115px;height:113px;flex:none}
.episode-body{position:relative;flex:1;background:
  repeating-linear-gradient(90deg,transparent 0 2px,#e3e6e7 2px 3px) bottom/100% 26px no-repeat,var(--white)}
.episode-play{position:absolute;left:24px;top:24px;width:30px;height:30px}
.episode-title{position:absolute;left:66px;top:23px;width:210px;font-family:"Poppins",sans-serif;font-weight:500;font-size:12.2px;line-height:17.5px;color:#222}
.episode-time{position:absolute;right:22px;top:21px;font-size:11px;color:#444}
.view-all{left:556px;top:668px;width:88px;height:34px;border:2px solid var(--btn);color:var(--ink);font-family:"Poppins",sans-serif;font-weight:600;font-size:11px;display:flex;align-items:center;justify-content:center}

/* support */
.support{top:2361px;height:458px}
.support-photo{left:161px;top:55px;width:349px;height:349px;border-radius:50%;background:radial-gradient(circle at 35% 45%,#4c5a66 0%,#a7998d 45%,#e8d6c9 100%)}
.support-title{left:596px;top:55px;font-size:20px;font-weight:600}
.support .rule{left:596px;top:91px;width:94px}
.support-copy{left:597px;top:138px;width:448px;font-size:14.4px;line-height:24px;color:#3a3f40}
.support .btn{left:600px;top:343px;width:135px;height:44px;font-size:12.5px}

/* contact */
.contact{top:2819px;height:515px;background:linear-gradient(100deg,#8a7462 0%,#a48c78 40%,#b59a83 70%,#8d7560 100%)}
.contact-scene{left:500px;top:30px;width:700px;height:485px;background:linear-gradient(160deg,rgba(40,40,44,.0) 0%,rgba(40,40,44,.25) 60%,rgba(200,150,60,.25) 100%)}
.contact-title{left:132px;top:90px;font-size:20px;font-weight:700;color:var(--white)}
.contact .rule{left:132px;top:128px;width:86px;background:var(--white)}
.field{left:131px;width:310px;height:47px;background:var(--white);border:none;padding:0 14px;font-family:"Mulish",sans-serif;font-size:13px;color:#444;display:flex;align-items:center}
.contact .btn{left:131px;top:345px;width:310px;height:47px;font-size:18px;font-weight:700}

/* footer */
.site-footer{top:3334px;height:115px}
.footer-brand{left:134px;top:26px;font-family:"Poppins",sans-serif;font-weight:600;color:var(--brand);font-size:36px;display:flex;align-items:center;gap:10px}
.footer-brand .brand-dot{width:14px;height:14px}
.footer-contact{left:588px;top:42px;display:flex;align-items:center;gap:8px;font-size:11.5px;color:#333}
.footer-contact svg{width:11px;height:11px}
.footer-contact .gap{width:18px}
.social{width:20px;height:20px;border-radius:50%}
.copyright{right:134px;top:84px;font-size:9.5px;color:#555}
</style>
</head>
<body>

<header class="site-header">
  <div class="brand-name"><span class="brand-dot"></span>Calm Harbor</div>
</header>

<section class="hero" role="img" aria-label="Video still: a therapist recording a message in a bright apartment">
  <svg class="abs hero-play" viewBox="0 0 52 52"><circle cx="26" cy="26" r="23" fill="none" stroke="#fff" stroke-width="3"/><path d="M21 16 L37 26 L21 36 Z" fill="#fff"/></svg>
  <div class="abs hero-title">EMOTIONAL AND PSYCHOLOGICAL</div>
</section>

<section class="welcome">
  <h2 class="abs welcome-kicker">WELCOME TO</h2>
  <h2 class="abs welcome-title">CALM HARBOR</h2>
  <span class="abs rule"></span>
  <p class="abs welcome-copy">There are many variations of passages of Lorem Ipsum available, but the majority have suffered alteration in some form, by injected humour, or randomised words which don't look even slightly believable. If you are going to use a passage of Lorem Ipsum, you need to be sure there isn't anything embarrassing hidden in the middle of text. All the Lorem Ipsum generators on the Internet tend to repeat predefined chunks as necessary, making this the first true generator on the Internet. It uses a dictionary of over 200 Latin words, combined</p>
  <a class="btn">Read More</a>
  <div class="abs welcome-photo" role="img" aria-label="Laptop on a desk showing an online session with a therapist at a whiteboard"></div>
</section>

<section class="therapists">
  <h2 class="abs section-title">QUALIFIED THERAPISTS</h2>
  <span class="abs section-rule"></span>
  <svg class="abs carousel-arrow" style="left:72px" viewBox="0 0 22 30"><path d="M16 4 L6 15 L16 26" fill="none" stroke="#8fc3d2" stroke-width="3"/></svg>
  <svg class="abs carousel-arrow" style="left:1108px" viewBox="0 0 22 30"><path d="M6 4 L16 15 L6 26" fill="none" stroke="#8fc3d2" stroke-width="3"/></svg>

  <article class="abs therapist-card" style="left:134px">
    <div class="therapist-photo" role="img" aria-label="Portrait of a smiling therapist wearing a headset" style="background:linear-gradient(135deg,#6d6a66,#c9b7b6)"></div>
    <div class="therapist-name">Daniel</div><div class="therapist-role">Trainer</div>
    <p class="therapist-bio">There are many variations of passages of Lorem Ipsum avail able, but the majority have suffered alteration</p>
    <a class="btn">View Bio</a>
  </article>
  <article class="abs therapist-card" style="left:370px">
    <div class="therapist-photo" role="img" aria-label="Portrait of a therapist wearing headphones" style="background:linear-gradient(135deg,#d9d6d0,#e7a6b0)"></div>
    <div class="therapist-name">Mark Ellis</div><div class="therapist-role">Trainer</div>
    <p class="therapist-bio">There are many variations of passages of Lorem Ipsum avail able, but the majority have suffered alteration</p>
    <a class="btn">View Bio</a>
  </article>
  <article class="abs therapist-card" style="left:607px">
    <div class="therapist-photo" role="img" aria-label="Portrait of a therapist taking notes with a headset" style="background:linear-gradient(135deg,#5a463c,#a78a7d)"></div>
    <div class="therapist-name">Stanley Rowe</div><div class="therapist-role">Trainer</div>
    <p class="therapist-bio">There are many variations of passages of Lorem Ipsum avail able, but the majority have suffered alteration</p>
    <a class="btn">View Bio</a>
  </article>
  <article class="abs therapist-card" style="left:845px">
    <div class="therapist-photo" role="img" aria-label="Portrait of a therapist gesturing while speaking" style="background:linear-gradient(135deg,#e6e1da,#7a7670)"></div>
    <div class="therapist-name">Tobias</div><div class="therapist-role">Trainer</div>
    <p class="therapist-bio">There are many variations of passages of Lorem Ipsum avail able, but the majority have suffered alteration</p>
    <a class="btn">View Bio</a>
  </article>
</section>

<section class="podcasts">
  <h2 class="abs section-title">PODCASTS</h2>
  <span class="abs section-rule"></span>

  <article class="abs episode" style="left:131px;top:127px">
    <div class="episode-photo" role="img" aria-label="Host smiling at a laptop" style="background:linear-gradient(135deg,#c9b3a8,#f0e6e2)"></div>
    <div class="episode-body"><svg class="episode-play" viewBox="0 0 30 30"><circle cx="15" cy="15" r="15" fill="var(--red)"/><path d="M12 9 L21 15 L12 21 Z" fill="#fff"/></svg><div class="episode-title">Tranquility Talks: Finding Inner Peace and Contentment</div><div class="episode-time">05.45</div></div>
  </article>
  <article class="abs episode" style="left:611px;top:127px">
    <div class="episode-photo" role="img" aria-label="Host resting chin on hand" style="background:linear-gradient(135deg,#3b3a38,#a59c90)"></div>
    <div class="episode-body"><svg class="episode-play" viewBox="0 0 30 30"><circle cx="15" cy="15" r="15" fill="var(--red)"/><path d="M12 9 L21 15 L12 21 Z" fill="#fff"/></svg><div class="episode-title">The Peaceful Mindset: Navigating Life's Challenges with Clarity and Calmness</div><div class="episode-time">05.45</div></div>
  </article>
  <article class="abs episode" style="left:131px;top:257px">
    <div class="episode-photo" role="img" aria-label="Host with headset beside a plant" style="background:linear-gradient(135deg,#8ea36b,#c8ccd0)"></div>
    <div class="episode-body"><svg class="episode-play" viewBox="0 0 30 30"><circle cx="15" cy="15" r="15" fill="var(--red)"/><path d="M12 9 L21 15 L12 21 Z" fill="#fff"/></svg><div class="episode-title">Meditation Matters: Cultivating Stillness and Serenity in a Busy World</div><div class="episode-time">05.45</div></div>
  </article>
  <article class="abs episode" style="left:611px;top:257px">
    <div class="episode-photo" role="img" aria-label="Host writing notes with a coffee cup" style="background:linear-gradient(135deg,#2c2a29,#d7d2cc)"></div>
    <div class="episode-body"><svg class="episode-play" viewBox="0 0 30 30"><circle cx="15" cy="15" r="15" fill="var(--red)"/><path d="M12 9 L21 15 L12 21 Z" fill="#fff"/></svg><div class="episode-title">The Art of Inner Peace: Strategies for Finding Harmony and Balance</div><div class="episode-time">05.45</div></div>
  </article>
  <article class="abs episode" style="left:131px;top:390px">
    <div class="episode-photo" role="img" aria-label="Host with headphones writing" style="background:linear-gradient(135deg,#dfe3e6,#4d6a9a)"></div>
    <div class="episode-body"><svg class="episode-play" viewBox="0 0 30 30"><circle cx="15" cy="15" r="15" fill="var(--red)"/><path d="M12 9 L21 15 L12 21 Z" fill="#fff"/></svg><div class="episode-title">The Zen Life: A Journey to Inner Peace and Self-Discovery</div><div class="episode-time">05.45</div></div>
  </article>
  <article class="abs episode" style="left:611px;top:390px">
    <div class="episode-photo" role="img" aria-label="Host with headset at a laptop" style="background:linear-gradient(135deg,#e7e4df,#4a6ea5)"></div>
    <div class="episode-body"><svg class="episode-play" viewBox="0 0 30 30"><circle cx="15" cy="15" r="15" fill="var(--red)"/><path d="M12 9 L21 15 L12 21 Z" fill="#fff"/></svg><div class="episode-title">Quiet the Mind, Empower the Soul: Achieving Tranquility in a Noisy World</div><div class="episode-time">05.45</div></div>
  </article>
  <article class="abs episode" style="left:131px;top:518px">
    <div class="episode-photo" role="img" aria-label="Host on a video call outdoors" style="background:linear-gradient(135deg,#4f7a4c,#c2b8a6)"></div>
    <div class="episode-body"><svg class="episode-play" viewBox="0 0 30 30"><circle cx="15" cy="15" r="15" fill="var(--red)"/><path d="M12 9 L21 15 L12 21 Z" fill="#fff"/></svg><div class="episode-title">The Power of Presence: Mindful Living for a More Peaceful Life</div><div class="episode-time">05.45</div></div>
  </article>
  <article class="abs episode" style="left:611px;top:518px">
    <div class="episode-photo" role="img" aria-label="Host working at a desk" style="background:linear-gradient(135deg,#b3b6b5,#e9e7e4)"></div>
    <div class="episode-body"><svg class="episode-play" viewBox="0 0 30 30"><circle cx="15" cy="15" r="15" fill="var(--red)"/><path d="M12 9 L21 15 L12 21 Z" fill="#fff"/></svg><div class="episode-title">Finding Peace in Turbulent Times: Coping with Stress and Anxiety in Today's World</div><div class="episode-time">05.45</div></div>
  </article>

  <a class="abs view-all">VIEW ALL</a>
</section>

<section class="support">
  <div class="abs support-photo" role="img" aria-label="Laptop showing a friendly video support session"></div>
  <h2 class="abs support-title">SUPPORT</h2>
  <span class="abs rule"></span>
  <p class="abs support-copy">There are many variations of passages of Lorem Ipsum available, but the majority have suffered alteration in some form, by injected humour, or randomised words which don't look even slightly believable. If you are going to use a passage of Lorem Ipsum, you need to be sure there isn't anything embarrassing hidden in the middle of text. All the Lorem Ipsum generators on the Internet tend to repeat predefined</p>
  <a class="btn">Get Support</a>
</section>

<section class="contact">
  <div class="abs contact-scene" role="img" aria-label="Hands typing on a laptop during a group video call, notepad and pencil on the desk"></div>
  <h2 class="abs contact-title">CONTACT US</h2>
  <span class="abs rule"></span>
  <div class="abs field" style="top:166px">First Name</div>
  <div class="abs field" style="top:222px">Last Name</div>
  <div class="abs field" style="top:279px">Email id</div>
  <a class="btn">Submit</a>
</section>

<footer class="site-footer">
  <div class="abs footer-brand"><span class="brand-dot"></span>Calm Harbor</div>
  <div class="abs footer-contact">
    <svg viewBox="0 0 12 12"><rect x="0.5" y="2" width="11" height="8" fill="#444"/><path d="M0.5 2 L6 6.5 L11.5 2" fill="none" stroke="#fff" stroke-width="1"/></svg>
    <span>hello@calmharbor.com</span><span class="gap"></span>
    <svg viewBox="0 0 12 12"><path d="M2 1 L4.5 1 L5.5 3.8 L4 5 Q5 7.5 7 8 L8.2 6.5 L11 7.5 L11 10 Q6 11.5 1.5 6 Q0.5 3 2 1Z" fill="#444"/></svg>
    <span>+1 555 010 0199</span><span class="gap"></span>
    <span>FOLLOW US</span>
    <span class="social" style="background:#3b5ba8"></span>
    <span class="social" style="background:#c5337c"></span>
    <span class="social" style="background:#e02b20"></span>
  </div>
  <div class="abs copyright">Copyright © 2023 All Rights Reserved</div>
</footer>

</body>
</html>
```